Company Mission & Values Poster

I'd like an A2 Portrait Poster displaying our company's Mission & Values.
See our website for our logo, fonts, mission & values.
https://talvendo.com.au/

Our Mission: Creating homes for abundant life
Values: Love, Thinking, Team, Zoe.

Some ideas to consider:
Mission as the Headline then
A logo for each of the 4 Values and the words

Target Market(s)

Myself & my team

Industry/Entity Type

Real Estate

Font styles to use
Other font styles liked:
• Company fonts as seen on our website

```html
<!DOCTYPE html>
<html lang="en">
<head>
<meta charset="utf-8">
<title>Talvendo — Mission &amp; Values Poster</title>
<link rel="stylesheet" href="https://fonts.googleapis.com/css2?family=Bodoni+Moda:wght@400;500&family=Nunito+Sans:wght@400;500&display=swap">
<style>
  :root {
    --page-bg: #efefed;
    --poster-green: #0c3a2c;
    --ink-light: #ffffff;
    --band-ink: #0c3a2c;
    --rule: rgba(255, 255, 255, 0.35);
    --icon-fill: #15493a;
    --serif: "Bodoni Moda", "Didot", serif;
    --sans: "Nunito Sans", "Helvetica Neue", sans-serif;
  }
  * { box-sizing: border-box; margin: 0; padding: 0; }
  html, body {
    width: 1200px; height: 1200px; overflow: hidden;
    background: var(--page-bg);
  }
  .poster {
    position: absolute; left: 216px; top: 40px;
    width: 768px; height: 1120px;
    background: var(--poster-green);
    color: var(--ink-light);
    box-shadow: 0 6px 18px rgba(0,0,0,0.18);
  }
  .brand {
    position: absolute; top: 50px; left: 0; right: 0;
    display: flex; justify-content: center; align-items: center; gap: 22px;
  }
  .brand-dot {
    width: 58px; height: 58px; border-radius: 50%;
    border: 3px solid var(--ink-light);
  }
  .brand-name {
    font-family: var(--serif); font-weight: 400;
    font-size: 76px; line-height: 1; letter-spacing: 8px;
  }
  .title-band {
    position: absolute; top: 167px; left: 0; right: 0; height: 48px;
    background: var(--ink-light); color: var(--band-ink);
    display: flex; align-items: center; justify-content: center;
    font-family: var(--serif); font-size: 32px; letter-spacing: 2px;
  }
  .mission-label, .values-label {
    position: absolute; left: 0; right: 0; text-align: center;
    font-family: var(--sans); font-weight: 500; font-size: 19px; letter-spacing: 0.5px;
  }
  .mission-label { top: 258px; }
  .values-label { top: 396px; }
  .mission-statement {
    position: absolute; top: 292px; left: 0; right: 0; text-align: center;
    font-family: var(--serif); font-size: 29px; letter-spacing: 1.5px;
  }
  .value {
    position: absolute; left: 0; right: 0; height: 160px;
  }
  .value-icon {
    position: absolute; left: 31px; width: 100px; height: 100px;
  }
  .value-title {
    position: absolute; left: 160px; top: 0;
    font-family: var(--serif); font-size: 28px; letter-spacing: 1px; line-height: 1;
  }
  .value-text {
    position: absolute; left: 160px; width: 560px;
    font-family: var(--sans); font-size: 16px; line-height: 25.5px;
    text-align: justify; letter-spacing: -0.1px;
  }
  .divider {
    position: absolute; left: 42px; width: 674px; height: 1px;
    background: var(--rule);
  }
  .value--love     { top: 416px; }
  .value--thinking { top: 571px; }
  .value--team     { top: 736px; }
  .value--zoe      { top: 910px; }
  .value--love .value-icon     { top: 12px; }
  .value--thinking .value-icon { top: 22px; }
  .value--team .value-icon     { top: 22px; }
  .value--zoe .value-icon      { top: 19px; }
  .value--love .value-text     { top: 40px; }
  .value--thinking .value-text { top: 48px; }
  .value--team .value-text     { top: 48px; }
  .value--zoe .value-text      { top: 47px; }
</style>
</head>
<body>
<main class="poster">
  <header class="brand">
    <span class="brand-dot"></span>
    <span class="brand-name">TALVENDO</span>
  </header>

  <div class="title-band">MISSION &amp; VALUES</div>

  <p class="mission-label">OUR MISSION:</p>
  <h1 class="mission-statement">CREATING HOMES FOR ABUNDANT LIFE</h1>

  <p class="values-label">VALUES:</p>

  <section class="value value--love">
    <svg class="value-icon" viewBox="0 0 100 100" role="img" aria-label="Icon: heart held in an open hand">
      <circle cx="50" cy="50" r="47" fill="none" stroke="#fff" stroke-width="3"/>
      <circle cx="50" cy="50" r="30" fill="var(--icon-fill)"/>
    </svg>
    <h2 class="value-title">LOVE</h2>
    <p class="value-text">Our mission is founded in our love and respect for people - those we develop for, those in our teams and those in the communities we create and operate within.</p>
  </section>
  <div class="divider" style="top:554px"></div>

  <section class="value value--thinking">
    <svg class="value-icon" viewBox="0 0 100 100" role="img" aria-label="Icon: glowing light bulb">
      <circle cx="50" cy="50" r="47" fill="none" stroke="#fff" stroke-width="3"/>
      <circle cx="50" cy="50" r="30" fill="var(--icon-fill)"/>
    </svg>
    <h2 class="value-title">THINKING</h2>
    <p class="value-text">We believe in the power of thinking. Our rigorous and creative processes create beautifully considered solutions for our purchasers, the communities we develop within and the environment.</p>
  </section>
  <div class="divider" style="top:720px"></div>

  <section class="value value--team">
    <svg class="value-icon" viewBox="0 0 100 100" role="img" aria-label="Icon: three hands joining together">
      <circle cx="50" cy="50" r="47" fill="none" stroke="#fff" stroke-width="3"/>
      <circle cx="50" cy="50" r="30" fill="var(--icon-fill)"/>
    </svg>
    <h2 class="value-title">TEAM</h2>
    <p class="value-text">Property development is a team sport. We surround ourselves with the best designers and advisers. We strive to create an environment that allows them to do their best work and love doing it.</p>
  </section>
  <div class="divider" style="top:893px"></div>

  <section class="value value--zoe">
    <svg class="value-icon" viewBox="0 0 100 100" role="img" aria-label="Icon: young plant held in an open hand">
      <circle cx="50" cy="50" r="47" fill="none" stroke="#fff" stroke-width="3"/>
      <circle cx="50" cy="50" r="30" fill="var(--icon-fill)"/>
    </svg>
    <h2 class="value-title">ZOE</h2>
    <p class="value-text">Our mission is to create places for ‘Zoe’ - the Greek word for abundant life. We do this through exquisite design, quality construction and celebrating nature.</p>
  </section>
</main>
</body>
</html>
```